Tennis String Package

Need a design for a tennis string package.
Design to be 15 cm in length and width.
I would like to create a style like the one in the image.
Brand name VUMEX
Product name SKYBOUND
Front and back designs are required.

Colors
0054AA
0677BA
7BADD7
CADEEF
E8F1F8
A7469A
B969AE
D3A5CF
EDDBEB
F8F0F9
6B429C
8869AF
B7A5CE
E3DAEB
F3F0F8

```html
<!DOCTYPE html>
<html lang="en">
<head>
<meta charset="utf-8">
<title>VUMEX SKYBOUND – String Package</title>
<link href="https://fonts.googleapis.com/css2?family=Jost:wght@300;400&display=swap" rel="stylesheet">
<style>
  :root {
    --page: #ffffff;
    --sky-top: #7e7f93;
    --sky-mid: #76809a;
    --sky-low: #8590a3;
    --sky-glow: #a9a6b0;
    --ink: #ffffff;
    --ink-soft: rgba(255,255,255,0.55);
  }
  html, body {
    margin: 0;
    padding: 0;
    width: 1200px;
    height: 1200px;
    overflow: hidden;
    background: var(--page);
  }
  .canvas {
    position: relative;
    width: 1200px;
    height: 1200px;
    background: var(--page);
    font-family: 'Jost', sans-serif;
  }
  .package-front {
    position: absolute;
    left: 191px;
    top: 191px;
    width: 818px;
    height: 818px;
    overflow: hidden;
  }
  .sky-backdrop {
    position: absolute;
    inset: 0;
    width: 100%;
    height: 100%;
  }
  .brand-name {
    position: absolute;
    left: 111px;
    top: 278px;
    margin: 0;
    font-weight: 400;
    font-size: 38px;
    letter-spacing: 17px;
    color: var(--ink);
    line-height: 1;
  }
  .product-name {
    position: absolute;
    left: 552px;
    top: 289px;
    margin: 0;
    font-weight: 400;
    font-size: 22px;
    letter-spacing: 8px;
    color: var(--ink);
    line-height: 1;
  }
  .subtitle {
    position: absolute;
    left: 111px;
    top: 378px;
    margin: 0;
    font-weight: 300;
    font-size: 13px;
    letter-spacing: 2px;
    color: var(--ink-soft);
  }
  .description {
    position: absolute;
    left: 112px;
    top: 448px;
    width: 260px;
    margin: 0;
    font-weight: 400;
    font-size: 10.5px;
    line-height: 15px;
    letter-spacing: 1.6px;
    color: var(--ink);
  }
</style>
</head>
<body>
  <div class="canvas">
    <section class="package-front">
      <svg class="sky-backdrop" viewBox="0 0 818 818" preserveAspectRatio="none" role="img" aria-label="Soft photograph of a hazy lilac and blue evening sky with streaked clouds">
        <defs>
          <linearGradient id="skyBase" x1="0" y1="0" x2="1" y2="1">
            <stop offset="0" stop-color="#83839a"/>
            <stop offset="0.35" stop-color="#77798e"/>
            <stop offset="0.6" stop-color="#7d879b"/>
            <stop offset="1" stop-color="#9c9aa6"/>
          </linearGradient>
          <radialGradient id="skyGlow" cx="1" cy="1" r="0.45">
            <stop offset="0" stop-color="#b3adb5" stop-opacity="0.9"/>
            <stop offset="1" stop-color="#b3adb5" stop-opacity="0"/>
          </radialGradient>
          <radialGradient id="skyBlue" cx="0.3" cy="0.65" r="0.4">
            <stop offset="0" stop-color="#6d7598" stop-opacity="0.6"/>
            <stop offset="1" stop-color="#6d7598" stop-opacity="0"/>
          </radialGradient>
        </defs>
        <rect width="818" height="818" fill="url(#skyBase)"/>
        <rect width="818" height="818" fill="url(#skyBlue)"/>
        <rect width="818" height="818" fill="url(#skyGlow)"/>
      </svg>
      <h1 class="brand-name">VUMEX</h1>
      <h2 class="product-name">SKYBOUND</h2>
      <p class="subtitle">Lorem Ipsum</p>
      <p class="description">Lorem ipsum dolor sit amet, consectetur adipiscing elit, sed do eiusmod tempor incididunt ut labore et dolore magna aliqua. Quis ipsum suspendisse ultrices gravida. Risus commodo</p>
    </section>
  </div>
</body>
</html>
```